Asphalt Driveway Billboard Design

We need a billboard designed for an Asphalt & Concrete Company in Minnesota. We want to advertise Asphalt Driveways on this billboard! Logo is uploaded below. Our website is pinecrest-paving.net for more information.

```html
<!DOCTYPE html>
<html lang="en">
<head>
<meta charset="utf-8">
<title>Pinecrest Paving &amp; Concrete – Billboard</title>
<link href="https://fonts.googleapis.com/css2?family=Montserrat:wght@600;700;800&display=swap" rel="stylesheet">
<style>
  :root {
    --page-bg: #eef1f5;
    --white: #ffffff;
    --ink: #1c1c1e;
    --brand-blue: #0b4f9c;
    --deep-blue: #0a3f80;
    --accent-blue: #2a86d6;
    --light-blue: #7cc3f5;
    --photo-house: #6b7a70;
    --photo-drive: #8a8d93;
    --photo-asphalt: #2d3138;
    --photo-brick: #9b6a52;
  }
  html, body {
    margin: 0;
    width: 1200px;
    height: 1200px;
    overflow: hidden;
    background: var(--page-bg);
  }
  .billboard {
    position: absolute;
    left: 0;
    top: 412px;
    width: 1200px;
    height: 375px;
    background: var(--white);
    font-family: "Montserrat", sans-serif;
  }
  .billboard-art {
    position: absolute;
    inset: 0;
  }
  .brand {
    position: absolute;
    left: 280px;
    top: 78px;
    width: 380px;
    text-align: center;
    color: var(--ink);
  }
  .brand-mark {
    display: inline-block;
    width: 34px;
    height: 34px;
    background: var(--brand-blue);
    vertical-align: middle;
    margin-right: 10px;
  }
  .brand-name {
    font-weight: 800;
    font-size: 44px;
    letter-spacing: 1px;
    vertical-align: middle;
  }
  .brand-sub {
    font-weight: 700;
    font-size: 15px;
    letter-spacing: 2px;
    margin-top: 4px;
  }
  .headline {
    position: absolute;
    left: 250px;
    top: 184px;
    width: 420px;
    margin: 0;
    text-align: center;
    color: var(--brand-blue);
    font-weight: 800;
    font-size: 36px;
    line-height: 1.08;
  }
  .site-url {
    position: absolute;
    left: 195px;
    top: 310px;
    padding: 6px 14px;
    background: var(--brand-blue);
    color: var(--white);
    border-radius: 5px;
    font-weight: 700;
    font-size: 23px;
  }
  .cta {
    position: absolute;
    right: 22px;
    top: 280px;
    display: flex;
    align-items: center;
    gap: 14px;
  }
  .cta-label {
    color: var(--light-blue);
    font-weight: 700;
    font-size: 16px;
    line-height: 1.15;
    text-align: right;
  }
  .cta-phone {
    color: var(--white);
    font-weight: 800;
    font-size: 48px;
    letter-spacing: 0.5px;
  }
</style>
</head>
<body>
  <section class="billboard">
    <svg class="billboard-art" viewBox="0 0 1200 375" width="1200" height="375">
      <defs>
        <linearGradient id="houseLeft" x1="0" y1="0" x2="0" y2="1">
          <stop offset="0" stop-color="#4f6b44"/>
          <stop offset="0.4" stop-color="var(--photo-house)"/>
          <stop offset="0.62" stop-color="#8e8f92"/>
          <stop offset="1" stop-color="var(--photo-drive)"/>
        </linearGradient>
        <linearGradient id="houseRight" x1="0" y1="0" x2="0" y2="1">
          <stop offset="0" stop-color="#d8d2c8"/>
          <stop offset="0.5" stop-color="var(--photo-brick)"/>
          <stop offset="0.62" stop-color="#3a3e45"/>
          <stop offset="1" stop-color="var(--photo-asphalt)"/>
        </linearGradient>
      </defs>
      <polygon class="photo-left" points="0,0 260,0 90,375 0,375" fill="url(#houseLeft)" role="img" aria-label="Photo of a grey two-storey home with a freshly paved driveway"/>
      <polygon class="stripe-left" points="260,0 285,0 115,375 90,375" fill="var(--accent-blue)"/>
      <polygon class="stripe-left-thin" points="285,0 293,0 123,375 115,375" fill="var(--brand-blue)" opacity="0.5"/>
      <polygon class="panel-soft" points="580,0 780,0 620,375 420,375" fill="#e6eef6" opacity="0.6"/>
      <polygon class="photo-right" points="780,0 1200,0 1200,250 690,250" fill="url(#houseRight)" role="img" aria-label="Photo of a home with a garage and a new black asphalt driveway"/>
      <polygon class="band-edge" points="690,250 725,250 665,375 620,375" fill="var(--accent-blue)"/>
      <polygon class="cta-band" points="720,250 1200,250 1200,375 660,375" fill="var(--brand-blue)"/>
      <polygon class="cta-band-shade" points="920,250 1200,250 1200,375 880,375" fill="var(--deep-blue)" opacity="0.35"/>
    </svg>

    <div class="brand">
      <span class="brand-mark"></span><span class="brand-name">PINECREST</span>
      <div class="brand-sub">— PAVING &amp; CONCRETE —</div>
    </div>

    <h1 class="headline">ASPHALT DRIVEWAY<br>SPECIALISTS</h1>

    <div class="site-url">www.pinecrest-paving.net</div>

    <div class="cta">
      <div class="cta-label">REQUEST A<br>FREE ESTIMATE</div>
      <div class="cta-phone">763-555-0142</div>
    </div>
  </section>
</body>
</html>
```